Creation of design for a line of dietary supplements - 18 products

18 packages must be made in the same style, maintaining (maybe a slight change) the color scheme. All texts and their position, font and size must be preserved. The main graphic element is the nanoliposomal shell. In any form - voluminous, flat, but it must be conveyed in every design. The logo and flower must remain the same size.

Дизайн выглядит одинаково

Дизайн выглядит одинаково

Дизайн выглядит одинаково

```html
<!DOCTYPE html>
<html lang="en">
<head>
<meta charset="utf-8">
<title>K417 Oxivance – Antioxidants Complex Package Front</title>
<link rel="stylesheet" href="https://fonts.googleapis.com/css2?family=Poppins:ital,wght@0,400;0,500;0,600;0,700;1,400;1,600&display=swap">
<style>
  :root {
    --page-bg: #ecebee;
    --card-white: #ffffff;
    --ink: #141414;
    --magenta-light: #c94fbb;
    --magenta-deep: #7c2a70;
    --lavender: #d9c6de;
    --lavender-mid: #b89cc3;
    --shell-fill: #e7d7ea;
    --violet-band-start: #b06cc0;
    --violet-band-end: #7a4a8c;
    --band-text: #f1e4f5;
    --fine-ink: #6d6d6d;
    --fine-strong: #555555;
  }
  * { box-sizing: border-box; margin: 0; padding: 0; }
  html, body {
    width: 1200px; height: 960px; overflow: hidden;
    background: var(--page-bg);
    font-family: "Poppins", Arial, sans-serif;
  }
  .package-front {
    position: absolute; left: 50px; top: 130px;
    width: 1100px; height: 700px;
    background: var(--card-white);
    box-shadow: 0 10px 30px rgba(0,0,0,.12);
    overflow: hidden;
  }
  .package-shapes { position: absolute; inset: 0; }
  .shell-artwork { position: absolute; left: 700px; top: 110px; }
  .product-title {
    position: absolute; left: 70px; top: 40px;
    font-weight: 700; font-size: 92px; line-height: 0.92;
    color: var(--ink); letter-spacing: 1px;
  }
  .band-text { position: absolute; left: 80px; top: 262px; color: #fff; }
  .band-text .headline { font-weight: 700; font-size: 36px; letter-spacing: 0.5px; }
  .band-text .subline { font-weight: 500; font-size: 25px; line-height: 1.2; margin-top: 8px; letter-spacing: 1px; }
  .capsule-count {
    position: absolute; right: 50px; top: 444px; text-align: center; color: var(--ink);
  }
  .capsule-count .count { font-weight: 700; font-size: 46px; line-height: 1; }
  .capsule-count .unit { font-weight: 500; font-size: 20px; letter-spacing: 1px; }
  .supplement-label {
    position: absolute; left: 100px; top: 458px;
    font-weight: 500; font-size: 23px; color: var(--ink); letter-spacing: 0.5px;
  }
  .origin-line {
    position: absolute; left: 120px; top: 503px;
    font-weight: 500; font-size: 36px; color: var(--band-text); letter-spacing: 1px;
  }
  .maker-name {
    position: absolute; right: 40px; top: 588px;
    display: flex; align-items: center; gap: 10px;
    font-weight: 700; font-size: 22px; color: var(--ink); letter-spacing: 0.5px;
  }
  .maker-name .mark-dot { width: 16px; height: 16px; border-radius: 50%; background: var(--ink); }
  .fine-print {
    position: absolute; left: 100px; top: 576px;
    font-size: 11px; line-height: 1.25; color: var(--fine-ink); font-style: italic;
  }
  .fine-print strong { font-weight: 600; color: var(--fine-strong); }
  .fine-print .gap { margin-top: 6px; }
</style>
</head>
<body>
  <main class="package-front">
    <svg class="package-shapes" width="1100" height="700" viewBox="0 0 1100 700" aria-hidden="true">
      <defs>
        <linearGradient id="magentaBand" x1="0" x2="1" y1="0" y2="0">
          <stop offset="0" stop-color="var(--magenta-light)"/>
          <stop offset="1" stop-color="var(--magenta-deep)"/>
        </linearGradient>
        <linearGradient id="violetBand" x1="0" x2="1" y1="0" y2="0">
          <stop offset="0" stop-color="var(--violet-band-start)"/>
          <stop offset="1" stop-color="var(--violet-band-end)"/>
        </linearGradient>
      </defs>
      <rect x="0" y="236" width="1100" height="202" fill="var(--lavender)"/>
      <circle cx="840" cy="250" r="190" fill="var(--lavender-mid)"/>
      <rect x="0" y="250" width="1100" height="174" fill="url(#magentaBand)"/>
      <circle cx="840" cy="250" r="172" fill="url(#magentaBand)"/>
      <polygon points="0,492 880,492 960,562 0,562" fill="url(#violetBand)"/>
    </svg>

    <svg class="shell-artwork" width="280" height="280" viewBox="0 0 280 280"
         role="img" aria-label="Nanoliposome shell illustration">
      <circle cx="140" cy="140" r="138" fill="var(--card-white)"/>
      <circle cx="140" cy="140" r="126" fill="var(--shell-fill)"/>
    </svg>

    <h1 class="product-title">K417<br>OXIVANCE</h1>

    <div class="band-text">
      <p class="headline">ANTIOXIDANTS COMPLEX</p>
      <p class="subline">PROCESSED WITH<br>LIPOSOMAL NANOTECHNOLOGY</p>
    </div>

    <div class="capsule-count">
      <p class="count">30</p>
      <p class="unit">CAPSULES</p>
    </div>

    <p class="supplement-label">DIETARY SUPPLEMENT PRODUCT</p>
    <p class="origin-line">GENUINE PRODUCT OF THAILAND</p>

    <div class="maker-name"><span class="mark-dot"></span>VERALUNE BIOSCIENCE</div>

    <div class="fine-print">
      <p>Produced by</p>
      <p><strong>VERALUNE BIOSCIENCE CO., LTD.</strong></p>
      <p>88/12 Moo 4 Lotus Garden Rd. Soi 7, T.Bang Kaeo, A.Muang,</p>
      <p>Samutprakan 10270, Thailand. https://veralunebio.example/</p>
      <p class="gap">In association with</p>
      <p><strong>VERALUNE BIOSCIENCE UK LTD</strong> / Kent, United Kingdom</p>
      <p><strong>VERALUNE NANOCARE LLC</strong> / Oregon, United States of America</p>
      <p><strong>VERALUNE BIOSCIENCE EUROPE BV</strong> / Utrecht, Netherlands</p>
    </div>
  </main>
</body>
</html>
```